looking for sleek business card to standout from the crowd!

We are a young biotechnology company looking to help you personalize your health through understanding your genetic make up. We need you help in making a clean but sleek business card design using our new logo. The goal? Any time we give our cards out, people say "nice card!" The feel we are going for is "modern-techy". We don't want to come across as an old, giant pharma company, but not trying to be a hipster either.

Target Market(s)

healthcare and biotechnology industry.

Industry/Entity Type

Biotechnology

Contact Information for Business Card

Info to include on the card will be NAME, TITLE, EMAIL, PHONE. The companies website (www.corvalinbio.com) should also be on the card some where. Would like the logo, when printed, to be raised.

Requirements
Must have
• The logo we have attached in the color it is in. Fonts for text should lean toward more professional/tech.
Nice to have
• Prefer white/light color background
Should not have
• cartoons, landscape backgrounds images.

```html
<!DOCTYPE html>
<html lang="en">
<head>
<meta charset="utf-8">
<title>Corvalin Business Card</title>
<link rel="stylesheet" href="https://fonts.googleapis.com/css2?family=Open+Sans:wght@400;600;700&display=swap">
<style>
  :root {
    --stage: #f4f4f4;
    --card: #ffffff;
    --brand-blue: #1a75bf;
    --brand-green: #8cc63f;
    --ink: #4a4a4a;
    --ink-dark: #3d3d3d;
    --rule: #8a8a8a;
  }
  * { margin: 0; padding: 0; box-sizing: border-box; }
  html, body {
    width: 1200px;
    height: 1000px;
    overflow: hidden;
    background: var(--stage);
    font-family: "Open Sans", Arial, sans-serif;
  }
  .canvas { position: relative; width: 1200px; height: 1000px; }

  .business-card {
    position: absolute;
    left: 187px; top: 175px;
    width: 795px; height: 455px;
    background: var(--card);
    border-radius: 18px;
  }

  .wordmark {
    display: flex;
    align-items: center;
    gap: 12px;
  }
  .wordmark-name {
    color: var(--brand-blue);
    font-weight: 700;
    letter-spacing: 1px;
    line-height: 1;
  }
  .wordmark-dot {
    border-radius: 50%;
    background: var(--brand-green);
    flex: none;
  }

  .card-wordmark {
    position: absolute;
    left: 107px; top: 199px;
  }
  .card-wordmark .wordmark-name { font-size: 42px; }
  .card-wordmark .wordmark-dot { width: 34px; height: 34px; }

  .divider {
    position: absolute;
    left: 409px; top: 141px;
    width: 2px; height: 185px;
    background: var(--rule);
  }

  .contact-block {
    position: absolute;
    left: 433px; top: 134px;
  }
  .person-name {
    font-size: 26px;
    font-weight: 600;
    line-height: 1.1;
    color: var(--brand-blue);
  }
  .person-name .surname { color: var(--brand-green); }
  .person-title {
    font-size: 15px;
    font-weight: 700;
    color: var(--ink-dark);
    margin-top: 1px;
    letter-spacing: 0.2px;
  }
  .address {
    font-size: 18px;
    line-height: 22px;
    color: var(--ink);
    margin-top: 12px;
  }
  .contact-list {
    list-style: none;
    margin-top: 9px;
  }
  .contact-list li {
    display: flex;
    align-items: center;
    height: 27px;
    font-size: 18px;
    color: var(--ink);
  }
  .contact-list svg {
    width: 20px; height: 20px;
    margin-right: 14px;
    margin-left: -2px;
    flex: none;
  }
  .contact-list .site-name { color: var(--brand-blue); }

  .showcase-wordmark {
    position: absolute;
    left: 0; top: 808px;
    width: 1200px;
    height: 112px;
    justify-content: center;
    gap: 18px;
  }
  .showcase-wordmark .wordmark-name { font-size: 64px; }
  .showcase-wordmark .wordmark-dot { width: 52px; height: 52px; }
</style>
</head>
<body>
<main class="canvas">
  <section class="business-card">
    <div class="wordmark card-wordmark">
      <span class="wordmark-name">CORVALIN</span>
      <span class="wordmark-dot"></span>
    </div>

    <div class="divider"></div>

    <div class="contact-block">
      <h1 class="person-name">Daniel <span class="surname">Reyes</span></h1>
      <p class="person-title">CEO &amp; FOUNDER</p>
      <p class="address">Your Street Address,<br>Singapore, 1234</p>
      <ul class="contact-list">
        <li>
          <svg viewBox="0 0 20 20" aria-hidden="true">
            <circle cx="10" cy="10" r="10" fill="#8cc63f"/>
            <path d="M6.5 5.2l1.8-.4 1.1 2.6-1.2 1c.6 1.3 1.5 2.2 2.8 2.8l1-1.2 2.6 1.1-.4 1.8c-.2.5-.6.8-1.2.8C9.3 13.7 6.3 10.7 5.7 6.4c0-.6.3-1 .8-1.2z" fill="#fff"/>
          </svg>
          +000 123 456 789
        </li>
        <li>
          <svg viewBox="0 0 20 20" aria-hidden="true">
            <circle cx="10" cy="10" r="10" fill="#8cc63f"/>
            <rect x="5" y="6.5" width="10" height="7" rx="0.8" fill="#fff"/>
            <path d="M5.3 7l4.7 3.6L14.7 7" fill="none" stroke="#8cc63f" stroke-width="1"/>
          </svg>
          yourname@email.com
        </li>
        <li>
          <svg viewBox="0 0 20 20" aria-hidden="true">
            <circle cx="10" cy="10" r="10" fill="#8cc63f"/>
            <circle cx="11" cy="9" r="3.2" fill="none" stroke="#fff" stroke-width="1.6"/>
            <path d="M8.7 11.3L5.8 14.2" stroke="#fff" stroke-width="1.8" stroke-linecap="round"/>
          </svg>
          <span>www.<span class="site-name">corvalinbio</span>.com</span>
        </li>
      </ul>
    </div>
  </section>

  <div class="wordmark showcase-wordmark">
    <span class="wordmark-name">CORVALIN</span>
    <span class="wordmark-dot"></span>
  </div>
</main>
</body>
</html>
```